WEBSITE DESIGN, VELTRA paint and panel

We are in need of a website for Veltra Paint & Panel based in Brisbane, Australia. We are a boutique Automotive Paint & Panel Company that provides services to all makes and models of vehicles. We have attached a logo that is still in draft stage but gives you an idea of the colour scheme and fonts and overall impact we are looking for. We are after a white background so this is clean and crisp whilst being sleek, modern and professional. The website must represent our slogan of Flawless shade on the Finest frame. The website must therefore be visually effective as our product is to get colour and placement on vehicle body's correct so the website must have this impact on our clients. We are after a widescreen webpage that is simple and logical to navigate. The final design should give clients the confidence that we can deliver on our promise.
Updates

Target Market(s)

Vehicle Owners who have a need for panel repairs and people who want to reinvigorate their car with a new coat of paint.

Industry/Entity Type

Car Repair

Coding

Coded - Design and coding required

Number of Pages Required

5+ page

Font styles to use
Sans Serif

Colors
ffffff
ffc214
000000

Requirements
Must have
• Page 1 - Home Page
• Page 2 - Our Process
• Page 3 - Private Customers
• Page 4 - Fleet & Corporate
• Page 5 - Insurance
• Page 6 - Get a Quote
• Page 7 - Connect (Contacts Page)
• Same font and colour scheme as the logo.
Should not have
• A typical mechanical/paint and panel layout which looks like a template website.

```html
<!DOCTYPE html>
<html lang="en">
<head>
<meta charset="utf-8">
<title>Veltra Paint &amp; Panel</title>
<link rel="stylesheet" href="https://fonts.googleapis.com/css2?family=Lato:wght@400;700;900&family=Oswald:wght@500;700&display=swap">
<style>
:root{
  --yellow:#ffc214;
  --black:#000000;
  --ink:#1b1b1b;
  --dark:#222222;
  --darker:#141414;
  --grey:#6b6b6b;
  --light:#f2f2f2;
  --line:#dddddd;
  --white:#ffffff;
}
*{box-sizing:border-box;margin:0;padding:0}
html,body{width:1200px;height:2180px;overflow:hidden}
body{font-family:"Lato",sans-serif;color:var(--ink);background:var(--white);font-size:13px;line-height:1.5}
.wrap{width:1040px;margin:0 auto;position:relative}

/* top bar */
.topbar{height:32px;background:var(--darker);color:#bbb;font-size:11px}
.topbar .wrap{display:flex;justify-content:space-between;align-items:center;height:32px}
.topbar span{margin-right:26px}
.topbar b{color:var(--yellow);font-weight:700}

/* header */
.header{height:88px;background:var(--dark)}
.header .wrap{display:flex;justify-content:space-between;align-items:center;height:88px}
.logo{color:var(--yellow);font-weight:900;font-size:26px;line-height:1;letter-spacing:.5px;text-transform:uppercase}
.nav{display:flex}
.nav a{color:var(--white);text-decoration:none;font-size:12px;font-weight:700;padding:10px 14px}
.nav a.active{background:var(--yellow);color:var(--black)}

/* hero */
.hero{height:360px;position:relative;background:linear-gradient(100deg,#5b5e63 0%,#a9aaad 30%,#d9d9d9 55%,#b23a35 80%,#7d1d1c 100%)}
.hero-text{position:absolute;top:110px;left:0;right:0;text-align:center;color:var(--white)}
.hero-text h1{font-size:38px;font-weight:900;letter-spacing:1px;text-shadow:0 2px 6px rgba(0,0,0,.35)}
.hero-text p{font-size:20px;font-weight:700;margin-top:6px;text-shadow:0 2px 6px rgba(0,0,0,.35)}
.dots{position:absolute;right:80px;bottom:28px;display:flex;gap:6px}
.dots i{width:10px;height:10px;border-radius:50%;background:var(--white);display:block}
.dots i.on{background:var(--yellow)}

/* about */
.about{padding:46px 0 40px}
.about .wrap{display:flex;justify-content:space-between}
.about-copy{width:600px}
.about-copy h2{font-size:30px;font-weight:700;line-height:1.05;color:var(--black)}
.about-copy h2 span{display:block;color:var(--yellow);font-weight:900;font-size:30px}
.about-copy p{color:var(--grey);font-size:12px;margin-top:14px}
.quote{width:340px;background:var(--darker);padding:22px 22px 24px}
.quote h3{color:var(--white);font-size:16px;font-weight:700;margin-bottom:14px}
.quote .row{display:flex;gap:10px;margin-bottom:10px}
.quote .field{flex:1;height:30px;background:var(--white)}
.quote .area{height:70px;background:var(--white);margin-bottom:12px}
.quote .send{display:block;margin-left:auto;width:80px;height:30px;background:var(--yellow);color:var(--black);font-weight:900;font-size:12px;text-align:center;line-height:30px}

/* services */
.services .wrap{display:flex;justify-content:space-between;padding-top:14px}
.service{width:300px;text-align:center}
.service .photo{height:150px;margin-bottom:14px}
.service h4{color:var(--yellow);font-size:19px;font-weight:700}
.service p{color:var(--grey);font-size:12px;margin:6px 10px 8px}
.service a{color:var(--ink);font-size:11px;text-decoration:none}
.ph-polish{background:linear-gradient(135deg,#2d3340,#6b7486 60%,#c9ccd3)}
.ph-paint{background:linear-gradient(135deg,#9aa0a6,#e3e5e8 55%,#4a5f86)}
.ph-fleet{background:linear-gradient(135deg,#c2c6cc,#eff0f2 55%,#7b8390)}

/* special */
.special{padding-top:60px}
.section-title{text-align:center;font-size:24px;font-weight:900;color:var(--black);position:relative}
.section-title:after{content:"";display:block;width:900px;height:1px;background:var(--line);margin:-16px auto 0;position:relative;z-index:-1}
.section-title span{background:var(--white);padding:0 16px}
.special-grid{display:grid;grid-template-columns:340px 360px 340px;margin-top:40px;height:260px}
.col{display:flex;flex-direction:column;justify-content:space-around}
.feat{display:flex;gap:14px}
.feat svg{flex:none}
.feat h5{font-size:13px;font-weight:700;color:var(--black)}
.feat p{font-size:11px;color:var(--grey)}
.gun{margin:10px 30px;background:radial-gradient(circle at 50% 55%,#c9ced6,#eef0f3 55%,var(--white) 75%)}

/* info band */
.band{margin-top:40px;height:100px;background:var(--yellow)}
.band .wrap{display:flex;justify-content:space-between;align-items:center;height:100px;padding:0 70px}
.band-item{display:flex;align-items:center;gap:16px}
.band-item h6{font-size:26px;font-weight:900;color:var(--black);line-height:1.1}
.band-item p{font-size:12px;color:var(--black)}

/* process */
.process{padding-top:36px;height:240px}
.process .wrap{display:flex}
.process-intro{width:260px}
.process-intro h3{font-size:16px;font-weight:900;color:var(--black)}
.process-intro h3 span{display:block;font-family:"Oswald",sans-serif;color:var(--yellow);font-size:40px;line-height:1}
.process-intro p{font-size:11px;color:var(--grey);margin-top:8px}
.steps{flex:1;display:flex;justify-content:space-around}
.step{width:200px;text-align:center}
.step h4{font-size:18px;font-weight:900;color:var(--black);margin:8px 0 4px}
.step p{font-size:11px;color:var(--grey)}

/* footer */
.footer{background:var(--darker);color:#aaa;height:240px;font-size:11px}
.footer .wrap{display:flex;justify-content:space-between;padding-top:28px;height:200px}
.footer h5{color:var(--white);font-size:14px;font-weight:700;margin-bottom:12px}
.footer ul{list-style:none}
.footer li{margin-bottom:4px}
.testimonial{width:330px}
.testimonial p{margin-bottom:12px}
.person{display:flex;align-items:center;gap:10px}
.avatar{width:44px;height:44px;border-radius:50%;background:#555}
.person b{color:var(--white);display:block}
.contact{width:190px}
.social{display:flex;gap:8px;margin-top:8px}
.social i{width:14px;height:14px;background:var(--yellow);display:block}
.copyright{border-top:1px solid #333;text-align:center;line-height:40px;font-size:10px;color:#888}
</style>
</head>
<body>

<div class="topbar">
  <div class="wrap">
    <div><span><b>T</b> +61 7 3555 0148</span><span><b>A</b> 42 Kestrel Lane, Brisbane</span></div>
    <div><b>H</b> Mon-Fri 8:30am-5:30pm | Sat 9:00am-12:00pm</div>
  </div>
</div>

<header class="header">
  <div class="wrap">
    <div class="logo">Veltra Paint<br>&amp; Panel</div>
    <nav class="nav">
      <a class="active">Home</a><a>Our Process</a><a>Private Customers</a><a>Fleet &amp; Corporate</a><a>Insurance</a><a>Get a Quote</a><a>Connect</a>
    </nav>
  </div>
</header>

<section class="hero" role="img" aria-label="Photo of a painter spraying a red car panel in a workshop">
  <div class="hero-text">
    <h1>AENEAN SAPIEN PURUS, SAGITTIS</h1>
    <p>CRAS SODALES DUI VITAE EX DICTUM, SIT AMET MOLESTIE EX SODALES</p>
  </div>
  <div class="dots"><i class="on"></i><i></i><i></i><i></i></div>
</section>

<section class="about">
  <div class="wrap">
    <div class="about-copy">
      <h2>About<span>Veltra Paint &amp; Panel</span></h2>
      <p>Flawless shade on the finest frame. We are a boutique paint and panel workshop in Brisbane caring for every make and model. Our team matches colour with care, repairs panels with precision and returns each car looking as good as the day it left the factory floor.</p>
      <p>From small scratches to full resprays, we treat every job with the same attention. Clear quotes, honest timelines and a finish you can trust make us the first choice for drivers who value quality work.</p>
    </div>
    <form class="quote">
      <h3>Get Quick Quote</h3>
      <div class="row"><div class="field"></div><div class="field"></div></div>
      <div class="row"><div class="field"></div><div class="field"></div></div>
      <div class="area"></div>
      <span class="send">SEND</span>
    </form>
  </div>
</section>

<section class="services">
  <div class="wrap">
    <div class="service">
      <div class="photo ph-polish" role="img" aria-label="Photo of a car being polished"></div>
      <h4>Polishing &amp; Detailing</h4>
      <p>Deep clean and machine polish that brings back the gloss and protects paint for years to come.</p>
      <a>Read more...</a>
    </div>
    <div class="service">
      <div class="photo ph-paint" role="img" aria-label="Photo of a spray gun painting a car"></div>
      <h4>Auto Painting</h4>
      <p>Precise colour matching and spray booth finish for panels, touch ups and complete resprays.</p>
      <a>Read more...</a>
    </div>
    <div class="service">
      <div class="photo ph-fleet" role="img" aria-label="Photo of fleet vehicles in a workshop"></div>
      <h4>Fleet &amp; Industrial Services</h4>
      <p>Fast repair programs that keep company vehicles on the road and looking sharp every day.</p>
      <a>Read more...</a>
    </div>
  </div>
</section>

<section class="special">
  <div class="wrap">
    <h2 class="section-title"><span>OUR SPECIAL</span></h2>
    <div class="special-grid">
      <div class="col">
        <div class="feat">
          <svg width="30" height="30" viewBox="0 0 30 30"><circle cx="15" cy="12" r="8" fill="none" stroke="#000" stroke-width="2.5"/><path d="M10 18l-3 10 8-4 8 4-3-10" fill="#000"/></svg>
          <div><h5>Quality Repairs</h5><p>Every repair is checked by senior staff before hand over, so the finish meets our strict standard.</p></div>
        </div>
        <div class="feat">
          <svg width="30" height="30" viewBox="0 0 30 30"><path d="M4 4h11l12 12-11 11L4 15z" fill="#000"/><circle cx="10" cy="10" r="2.5" fill="#fff"/></svg>
          <div><h5>Low Price Range</h5><p>Fair, transparent pricing with no hidden costs, and a written quote before any work begins.</p></div>
        </div>
      </div>
      <div class="gun" role="img" aria-label="Illustration of a paint spray gun"></div>
      <div class="col">
        <div class="feat">
          <svg width="30" height="30" viewBox="0 0 30 30"><circle cx="15" cy="15" r="12" fill="none" stroke="#000" stroke-width="2.5"/><path d="M15 8v7l5 3" stroke="#000" stroke-width="2.5" fill="none"/></svg>
          <div><h5>Efficient Delivery Times</h5><p>Clear timelines and regular updates so you always know when your car will be ready.</p></div>
        </div>
        <div class="feat">
          <svg width="30" height="30" viewBox="0 0 30 30"><rect x="3" y="5" width="24" height="16" fill="none" stroke="#000" stroke-width="2.5"/><path d="M10 27h10M15 21v6" stroke="#000" stroke-width="2.5"/></svg>
          <div><h5>Latest Technological Equipment</h5><p>Modern spray booths and digital colour tools deliver a factory grade result every time.</p></div>
        </div>
      </div>
    </div>
  </div>
</section>

<section class="band">
  <div class="wrap">
    <div class="band-item">
      <svg width="44" height="44" viewBox="0 0 44 44"><circle cx="22" cy="22" r="18" fill="none" stroke="#000" stroke-width="3"/><path d="M22 11v11l8 5" stroke="#000" stroke-width="3" fill="none"/></svg>
      <div><h6>We Are Open</h6><p>Mon-Fri 8:30am-5:30pm &nbsp; Sat 9:00am-12:00pm</p></div>
    </div>
    <div class="band-item">
      <svg width="44" height="44" viewBox="0 0 44 44"><path d="M12 5l7 8-4 5c2 5 6 9 11 11l5-4 8 7-5 6C20 37 7 24 6 10z" fill="#000"/></svg>
      <div><h6>Call Us Anytime</h6><p>+61 7 3555 0148</p></div>
    </div>
  </div>
</section>

<section class="process">
  <div class="wrap">
    <div class="process-intro">
      <h3>OUR WORKING PROCESS<span>IN 3 STEPS</span></h3>
      <p>A simple path from first call to final polish. We inspect, explain and repair, keeping you informed at every stage of the job.</p>
    </div>
    <div class="steps">
      <div class="step">
        <svg width="44" height="44" viewBox="0 0 44 44"><path d="M22 4a12 12 0 0 0-7 22v5h14v-5A12 12 0 0 0 22 4z" fill="#000"/><rect x="16" y="34" width="12" height="4" fill="#000"/></svg>
        <h4>REVIEW</h4><p>We inspect the damage and talk through options with you.</p>
      </div>
      <div class="step">
        <svg width="44" height="44" viewBox="0 0 44 44"><path d="M10 4h18l8 8v28H10z" fill="#000"/><path d="M16 20h14M16 26h14M16 32h10" stroke="#fff" stroke-width="2.5"/></svg>
        <h4>REPORT</h4><p>You receive a clear written quote and repair plan.</p>
      </div>
      <div class="step">
        <svg width="44" height="44" viewBox="0 0 44 44"><path d="M6 30v-8l5-10h22l5 10v8z" fill="#000"/><rect x="6" y="30" width="7" height="6" fill="#000"/><rect x="31" y="30" width="7" height="6" fill="#000"/><circle cx="13" cy="24" r="3" fill="#fff"/><circle cx="31" cy="24" r="3" fill="#fff"/></svg>
        <h4>REPAIR</h4><p>Our team restores your car to a flawless finish.</p>
      </div>
    </div>
  </div>
</section>

<footer class="footer">
  <div class="wrap">
    <div class="testimonial">
      <h5>What People Say</h5>
      <p>"The colour match on my door was perfect and the car came back cleaner than when I dropped it off. Friendly team, honest price."</p>
      <div class="person">
        <div class="avatar" role="img" aria-label="Customer portrait"></div>
        <div><b>Daniel Harte</b>Manager, Fleet Hire</div>
      </div>
    </div>
    <div>
      <h5>Our Services</h5>
      <ul><li>Service 1</li><li>Service 2</li><li>Service 3</li><li>Service 4</li><li>Service 5</li></ul>
    </div>
    <div>
      <h5>Customer Success</h5>
      <ul><li>About Us</li><li>Our Team</li><li>Careers</li><li>Help Centre</li><li>Blog</li></ul>
    </div>
    <div class="contact">
      <h5>Contact Us</h5>
      <ul><li>42 Kestrel Lane</li><li>Brisbane QLD 4000</li><li>+61 7 3555 0148</li><li>hello@veltrapaint.example</li></ul>
      <div class="social"><i></i><i></i><i></i></div>
    </div>
  </div>
  <div class="copyright">Copyright &copy; Veltra Paint &amp; Panel. All rights reserved. Terms of use | Privacy policy</div>
</footer>

</body>
</html>
```